Web Design Project - Event Management Company

A web-page design needs to be created for an event management company. The logo has already been created, the design needs to draw on the themes and colors of the logo and extend on that.

The event management company likes to differentiate itself from others by being a bit "un-conventional" and being able to think outside the box.

the specialise in corporate events, weddings, AGMs, anything that requires coordination of resources. They also can provide Audio Visual services such as recording events.

final design will also require HTML implementation

```html
<!DOCTYPE html>
<html lang="en">
<head>
<meta charset="utf-8">
<title>Corner Piece Group — Dream Events</title>
<link href="https://fonts.googleapis.com/css2?family=Arimo:wght@400;700&family=Tinos:ital,wght@0,400;1,700&display=swap" rel="stylesheet">
<style>
:root{
  --ink:#000;
  --paper:#fff;
  --text:#f2f2f2;
  --muted:#bdbdbd;
  --dim:#5a5a5a;
  --nav:#0c0c0c;
  --tab-top:#2a2a2a;
  --tab-bottom:#0e0e0e;
  --photo-light:#d8d8d8;
  --photo-mid:#8d8d8d;
  --photo-dark:#3a3a3a;
}
*{margin:0;padding:0;box-sizing:border-box}
html,body{width:1200px;height:939px;overflow:hidden;background:var(--ink)}
body{position:relative;font-family:'Tinos',serif;color:var(--text)}
.hero-photo{position:absolute;inset:0;
  background:
    radial-gradient(ellipse 560px 430px at 600px 470px, rgba(150,150,150,.95) 0%, rgba(110,110,110,.85) 40%, rgba(40,40,40,.6) 75%, rgba(0,0,0,0) 100%),
    radial-gradient(ellipse 300px 380px at 880px 420px, rgba(200,200,200,.35), rgba(0,0,0,0) 100%),
    var(--ink);}
.main-nav{position:absolute;left:0;top:0;width:1200px;height:40px;background:linear-gradient(#111,#050505);border-bottom:1px solid #2a2a2a;box-shadow:0 2px 0 #000,0 3px 0 #1c1c1c}
.main-nav ul{list-style:none;display:flex;justify-content:center;align-items:center;height:34px;font-size:15px;letter-spacing:.2px}
.main-nav li{color:#9a9a9a}
.main-nav li+li::before{content:"–";color:#444;margin:0 26px}
.main-nav li.current{color:var(--paper)}
.brand-tab{position:absolute;left:467px;top:60px;width:262px;height:98px;
  background:linear-gradient(var(--tab-top),var(--tab-bottom));
  clip-path:polygon(0 0,100% 0,94% 100%,6% 100%);display:flex;flex-direction:column;align-items:center;justify-content:center;gap:10px}
.brand-mark{width:22px;height:22px;background:#e46a2b}
.brand-name{font-family:'Arimo',sans-serif;font-size:18px;color:#e6e6e6;letter-spacing:.3px}
.hero-title{position:absolute;top:258px;width:100%;text-align:center;font-family:'Arimo',sans-serif;font-weight:700;font-size:26px;color:var(--paper);text-shadow:0 2px 4px #000}
.hero-sub{position:absolute;top:302px;width:100%;text-align:center;font-family:'Arimo',sans-serif;font-size:19px;color:var(--paper);text-shadow:0 2px 4px #000;letter-spacing:-.2px}
.gallery-strip{position:absolute;top:346px;left:210px;display:flex;gap:16px}
.gallery-strip div{width:250px;height:143px;background:linear-gradient(135deg,var(--photo-light),var(--photo-mid) 55%,var(--photo-dark))}
.intro{position:absolute;top:504px;left:218px;width:772px;font-size:14px;line-height:16px;text-indent:30px;text-shadow:0 1px 2px #000}
.intro-link{position:absolute;top:566px;width:100%;text-align:center;font-style:italic;font-weight:700;font-size:13px;color:#c9c9c9;text-decoration:underline}
.section-title{position:absolute;top:616px;width:100%;text-align:center;font-family:'Arimo',sans-serif;font-size:40px;color:var(--paper);letter-spacing:-1px;text-shadow:0 2px 6px #000}
.about-col{position:absolute;top:669px;width:378px;font-size:14px;line-height:15.6px;text-shadow:0 1px 2px #000}
.about-col.left{left:215px}.about-col.right{left:620px}
.read-more{position:absolute;top:796px;left:551px;font-size:14px;color:var(--paper);border-bottom:1px solid var(--paper);padding-bottom:1px}
.footer-band{position:absolute;left:0;top:891px;width:1200px;height:48px;background:linear-gradient(#101010,#000)}
.slider-tab{position:absolute;left:476px;top:861px;width:253px;height:31px;background:linear-gradient(#2b2b2b,#111);clip-path:polygon(4% 0,96% 0,100% 100%,0 100%)}
.slider-dots{position:absolute;left:531px;top:874px;display:flex;gap:8px}
.slider-dots span{width:11px;height:11px;border-radius:50%;background:#080808;box-shadow:inset 0 1px 1px #000,0 1px 0 #333}
.slider-dots span.active{background:#777}
.legal{position:absolute;left:71px;top:909px;font-size:11px;color:var(--dim)}
.legal a{color:#9a9a9a;margin-left:22px;padding-left:12px;border-left:1px solid #444}
.social{position:absolute;left:1080px;top:901px;display:flex;gap:14px}
.social span{width:14px;height:14px;border-radius:50%;background:#5c5c5c}
</style>
</head>
<body>
<div class="hero-photo" role="img" aria-label="Soft black and white photograph of a wedding couple embracing, fading into black at the edges"></div>

<nav class="main-nav">
  <ul>
    <li class="current">HOME</li><li>ABOUT</li><li>SERVICES</li><li>EVENTS</li><li>GALLERY</li><li>VIDEO</li><li>CONTACTS</li>
  </ul>
</nav>

<header class="brand-tab">
  <span class="brand-mark"></span>
  <span class="brand-name">CORNER PIECE GROUP</span>
</header>

<h1 class="hero-title">DREAM EVENTS</h1>
<p class="hero-sub">WE CREATE UNFORGETTABLE IDEAS FOR YOU AND YOUR EVENT</p>

<section class="gallery-strip">
  <div role="img" aria-label="Bride and groom about to kiss"></div>
  <div role="img" aria-label="Joined hands with wedding rings over flowers"></div>
  <div role="img" aria-label="Bridal bouquet of tulips"></div>
</section>

<p class="intro">Lorem ipsum dolor sit amet, consectetur adipisicing elit, sed do eiusmod tempor incididunt ut labore et dolore magna aliqua. Ut enim ad minim veniam, quis nostrud exercitation ullamco laboris nisi ut aliquip ex ea commodo consequat. Duis aute irure dolor in reprehenderit in voluptate velit esse cillum dolore eu fugiat nulla pariatur.</p>
<p class="intro-link">Us eget lectus. Mauris justo. Curabitur nibh lectus, dapibus id, tempor eu, tempor non, erat.</p>

<h2 class="section-title">WHO WE ARE</h2>
<p class="about-col left">Lorem ipsum dolor sit amet, consectetur adipisicing elit, sed do eiusmod tempor incididunt ut labore et dolore magna aliqua. Ut enim ad minim veniam, quis nostrud exercitation ullamco laboris nisi ut aliquip ex ea commodo consequat. Duis aute irure dolor in reprehenderit in voluptate velit esse cillum dolore eu fugiat nulla pariatur. Excepteur sint occaecat cupidatat non proident, sunt in culpa qui officia deserunt mollit anim id est laborum.</p>
<p class="about-col right">Lorem ipsum dolor sit amet, consectetur adipisicing elit, sed do eiusmod tempor incididunt ut labore et dolore magna aliqua. Ut enim ad minim veniam, quis nostrud exercitation ullamco laboris nisi ut aliquip ex ea commodo consequat. Duis aute irure dolor in reprehenderit in voluptate velit esse cillum dolore eu fugiat nulla pariatur. Excepteur sint occaecat cupidatat non proident, sunt in culpa qui officia deserunt mollit anim id est laborum.</p>
<span class="read-more">Read more about us</span>

<footer>
  <div class="footer-band"></div>
  <div class="slider-tab"></div>
  <div class="slider-dots"><span></span><span class="active"></span><span></span><span></span><span></span><span></span><span></span><span></span></div>
  <p class="legal">Copyright © 2013. All rights reserved.<a>Privacy Policy</a></p>
  <div class="social" aria-label="Social links"><span></span><span></span><span></span><span></span></div>
</footer>
</body>
</html>
```